Milo Castell Moving DL Flyer

We need a double sided DL flyer to give to patients to let them know that we are moving location.
On one side we would like it to read:
"We Are Moving!" and "November 2017" and our logo.
On the other side we would like it to read:
"Same Great Staff"
"Same Great Service"
"Bigger, Brighter and Better"
"New Location at 42 Quarry Rd"
with a map below (attached)
The flyer should follow our practice branding. Attached is a copy of our business card as an example of this.

```html
<!DOCTYPE html>
<html lang="en">
<head>
<meta charset="utf-8">
<title>Milo Castell Optometry – We Are Moving</title>
<link rel="stylesheet" href="https://fonts.googleapis.com/css2?family=Crimson+Pro:wght@700&family=Montserrat:wght@400&display=swap">
<style>
  :root {
    --page-bg: #e8e5e1;
    --paper: #ffffff;
    --ink: #1e1e1e;
    --banner: #222222;
    --line: #3a3a3a;
    --muted: #6b6b6b;
    --photo-mid: #dfe2e2;
    --photo-dark: #5a6566;
  }
  * { margin: 0; padding: 0; box-sizing: border-box; }
  html, body {
    width: 1200px; height: 1200px; overflow: hidden;
    background: var(--page-bg);
  }
  .flyer {
    position: absolute; left: 360px; top: 40px;
    width: 480px; height: 1120px;
    background: var(--paper);
    overflow: hidden;
  }
  .photo {
    position: absolute; left: 0; top: 234px; width: 480px; height: 480px;
    background:
      radial-gradient(ellipse 70% 20% at 50% 55%, var(--photo-dark) 0%, rgba(90,101,102,0.35) 55%, transparent 100%),
      linear-gradient(180deg, var(--paper) 0%, var(--photo-mid) 30%, var(--photo-mid) 70%, var(--paper) 100%);
  }
  .banner {
    position: absolute; left: 38px; top: 0; width: 403px; height: 278px;
  }
  .headline {
    position: absolute; left: 38px; top: 22px; width: 403px;
    text-align: center;
    font-family: "Crimson Pro", Georgia, serif; font-weight: 700;
    font-size: 72px; line-height: 72px; color: var(--paper);
  }
  .date {
    position: absolute; left: 0; top: 706px; width: 480px;
    text-align: center;
    font-family: "Crimson Pro", Georgia, serif; font-weight: 700;
    font-size: 64px; line-height: 64px; color: var(--ink);
  }
  .house {
    position: absolute; left: 0; top: 840px; width: 480px; height: 280px;
  }
  .brand {
    position: absolute; left: 60px; top: 956px; width: 360px;
    text-align: center;
    font-family: "Crimson Pro", Georgia, serif; font-weight: 700;
    color: var(--ink);
  }
  .brand-name { font-size: 30px; line-height: 32px; }
  .brand-field { font-size: 48px; line-height: 50px; }
  .tagline {
    position: absolute; left: 60px; top: 1046px; width: 360px;
    text-align: center;
    font-family: "Montserrat", Arial, sans-serif; font-size: 15px; line-height: 18px;
    color: var(--muted);
  }
  .web-band {
    position: absolute; left: 38px; top: 1077px; width: 403px; height: 43px;
    background: var(--banner);
    color: var(--paper);
    font-family: "Montserrat", Arial, sans-serif; font-size: 17px;
    letter-spacing: 4px;
    display: flex; align-items: center; justify-content: center;
  }
</style>
</head>
<body>
  <div class="flyer">
    <div class="photo" role="img" aria-label="Photo of dark-framed glasses in front of a blurred eye test chart"></div>

    <svg class="banner" viewBox="0 0 403 278" aria-hidden="true">
      <polygon points="0,0 403,0 403,200 201.5,278 0,200" fill="var(--banner)"/>
    </svg>
    <h1 class="headline">We Are<br>Moving!</h1>

    <p class="date">November<br>2017</p>

    <svg class="house" viewBox="0 0 480 280" aria-hidden="true">
      <polyline points="38,237 53,79 239,6 426,79 441,237" fill="none" stroke="var(--line)" stroke-width="1.5"/>
    </svg>
    <div class="brand">
      <div class="brand-name">Milo Castell</div>
      <div class="brand-field">Optometry</div>
    </div>
    <p class="tagline">Clear Eyes. Clear Care.</p>

    <div class="web-band">www.milocastell.com.au</div>
  </div>
</body>
</html>
```